Design a Dynamic and User-Friendly Website for qGuestly: Revolutionize Visitor Management

Description of qGuestly:

qGuestly is an innovative online visitor management system designed to streamline the process of managing visitors in various organizational settings. Our system automates the check-in process, enhances security by keeping accurate visitor logs, and ensures compliance with local regulations through customizable features. With functionalities such as contactless sign-in, real-time notifications, visitor badge printing, and comprehensive reporting, qGuestly provides a modern solution to traditional visitor management challenges.

Target Audience:

Our primary target audience includes businesses and institutions across Africa, starting with Nigeria. This includes corporate offices, educational institutions, healthcare facilities, and government buildings that are looking for efficient, secure, and scalable visitor management solutions. Our system is particularly tailored to meet the needs of facility managers, security personnel, and front desk staff who prioritize ease of use, data security, and operational efficiency. Additionally, qGuestly aims to cater to IT managers looking for robust systems that can seamlessly integrate with existing organizational infrastructure.

Color Scheme:

While specific colors are not mandated, the chosen palette should convey trust and stability, growth and efficiency, and maintain a professional and clean appearance. The colors selected should harmonize to create a welcoming, secure, and efficient atmosphere.
Typography:

Use modern, sans-serif fonts for readability and a contemporary look. Primary text should be clear with high contrast against the background, and headings can be bold to create a hierarchical structure that is easy to navigate.
Imagery:

Photography: High-quality images that feature African professionals and contexts, illustrating diverse, professional scenarios relevant to our target industries (such as corporate offices, educational institutions, healthcare facilities). Photos should authentically represent the African demographic, showing interactions between people and technology, emphasizing the ease and security of the visitor management process.
Illustrations: Custom illustrations that should culturally resonate with African settings and characters, vividly depicting functionalities of qGuestly such as scanning a QR code, receiving a visitor badge, or receiving alerts on a smartphone or desktop. These illustrations should adopt a style that complements the overall design aesthetic of the site.
Layout and Design Elements:

A clean, minimalistic layout that focuses on usability with easy navigation paths for all user types.
Use cards or tiles for different sections such as features, testimonials, or case studies, which can help organize information cleanly and attractively.
Consider interactive elements like hover effects, animated transitions for loading elements, and subtle animations in illustrations to make the user experience dynamic and engaging.
Overall Theme:

The theme should be professional and welcoming, reflecting a high-tech solution that is approachable for users with varying levels of tech expertise. The design should instill confidence in the security and efficiency of the system, while also being culturally appropriate and user-friendly to encourage interaction and exploration of the site’s content.
This style and theme guide emphasizes flexibility in color usage while maintaining clear directives on the emotional and functional responses the design should invoke, ensuring it aligns with the values and needs of qGuestly's target audience.

What websites can designers draw inspiration from?
List websites you like and describe what you like about them.

https://entrypadhub.example/en-usremove
same industry so you can see their approaches to marketing to similar customers - granted their target is not specific to african market Very clean design and straight to the point. Their feature set is closest to our feature set.
http://www.gatelumo.exampleremove
clean design and straight to the point
http://lobbirant.exampleremove

Home Page
-------------------
Main Goal: Encourage visitors to start their 15-day free trial, effectively converting them into leads or potential customers.

Content Layout:
Hero Section: Engaging hero image or video that shows the qGuestly system in action, with clear, prominent call-to-action (CTA) buttons for "Start your 15 day free trial" and secondary CTA for "Buy now"

Product Overview: Quick introduction to what qGuestly is and its key benefits, such as enhanced security, easy integration, and improved operational efficiency.

Features Highlight: Brief visuals or icons depicting major features like contactless sign-in, real-time alerts, and comprehensive reporting.

How It Works: A concise step-by-step guide or graphic explaining how to get started with qGuestly.

CTA Section: A more detailed call to action for starting the free trial,
if they want a more hands on guide allow them to schedule a demo and if they are ready click purchase to buy now.
Footer: Navigation links to other site sections, social media links, and legal information.

-------------------
Pricing Page
-------------------
Main Goal: Clearly convey the pricing structure in a way that users can easily understand and compare options based on their location and specific needs.

Content Layout:

Pricing Introduction: Explain the subscription model, highlighting the flexibility and scalability of the service (i.e., per location and additional tablets).

Country-Specific Pricing Tabs: Tabs or a dropdown menu allowing users to choose their country (Nigeria, Ghana, South Africa, Kenya) to view localized pricing in the respective currencies (NGN, GHS, ZAR, KES).
Subscription Per Location: Detailed pricing for managing a single location, with benefits listed beside the price

Tablets and Data Plans: A clear breakdown of the cost per tablet and the associated wireless data plans, including bulk discount options if applicable.
Interactive Pricing Calculator: A tool that allows users to calculate their monthly cost based on the number of locations and tablets they plan to use.

Add ons - for hardware, etc

FAQs: A section dedicated to frequently asked questions specifically about pricing, billing cycles, and cancellation policies.

CTA: Strong call to action for starting a free trial, with an emphasis on the ease of signing up and the no-commitment nature of the trial.

Footer: Standard navigational links, contact information, and social media buttons.

-------------------
Feature Page Template
-------------------
Main Goal: To detail individual features of qGuestly, demonstrating the functionality and benefits to help prospective clients understand the value provided.

Content Layout:
Feature Introduction: Large title with a succinct description of the feature.

In-depth Details: Bullet points or short paragraphs explaining the feature, supported by relevant images or icons.

Use Case Scenario: Real-world application or a mini-case study showing the feature in action.

Benefit Summary: A list or graphic illustrating the benefits of the feature.

CTA: Prompt to try this feature via signup or schedule a demo speak with a sales representative.

Footer: Standard links and social media connections.

-------------------
Blog Page
-------------------
Main Goal: To engage current and prospective clients with useful content, position qGuestly as a thought leader in the visitor management space, and improve SEO rankings.

Content Layout:
Featured Article: Highlight a recent or popular post prominently at the top.

Article List: Thumbnails and summaries of additional articles with clear categorization (e.g., Tips, Case Studies, Industry News).

Search and Filter Tools: Allow users to filter blog posts by topic, date, etc.

Newsletter Signup: Encourage visitors to subscribe to updates.
Social Share Buttons: Enable easy sharing of articles.
Footer: Include a comprehensive footer with navigational links and contact info.

Generic Content Page (e.g., Contact Us, About Us)
------------------------------
Main Goal: To provide essential information about the qGuestly company or to facilitate contact with the company.

Content Layout:
Page Title and Introduction: Clear heading with a brief paragraph summarizing the page’s purpose.

Main Content Area: Detailed content appropriate to the page (e.g., company history, team bios for About Us; contact form, map, and helpline numbers for Contact Us).

Sidebar/Additional Elements: For Contact Us, include operational hours or a quick FAQ. For About Us, list awards or recognitions.

CTA: Depending on the page, direct users to other parts of the site (e.g., careers page link on About Us, newsletter sign-up on Contact Us).
Footer: Standard footer with expanded company details if on the Contact Us page.

Coding

```html
<!DOCTYPE html>
<html lang="en">
<head>
<meta charset="utf-8">
<title>qGuestly — Visitor Management</title>
<link rel="stylesheet" href="https://fonts.googleapis.com/css2?family=Figtree:wght@400;500;600;700&display=swap">
<style>
:root{
  --blue:#2a7fd4;
  --blue-deep:#1f6fc4;
  --ink:#2b2b2b;
  --text:#3a3a3a;
  --card:#cfe0fb;
  --card-soft:#d8e6fc;
  --dark:#333333;
  --purple:#5b0fa8;
  --white:#ffffff;
}
*{box-sizing:border-box;margin:0;padding:0}
html,body{width:1200px;height:4043px;overflow:hidden}
body{font-family:'Figtree',sans-serif;color:var(--text);background:var(--white);position:relative}
.abs{position:absolute}
.brand{font-size:36px;font-weight:500;color:var(--ink);display:flex;align-items:center;gap:10px}
.brand .dot{width:32px;height:32px;border-radius:50%;border:4px solid var(--blue)}
.btn{position:absolute;display:flex;align-items:center;justify-content:center;font-weight:700;font-size:14px;border-radius:5px}
.btn-solid{background:var(--blue);color:var(--white)}
.btn-line{border:1.5px solid var(--ink);color:var(--ink);background:transparent}
.hl{color:var(--blue)}
h1,h2,h3{font-weight:600;color:var(--ink)}
p{line-height:1.55}

/* hero */
.hero{position:absolute;left:0;top:0;width:1200px;height:819px;background:linear-gradient(180deg,#f6f9fe 0%,#dbe7fb 45%,#b9d1f6 100%)}
.nav-links{position:absolute;top:34px;left:475px;display:flex;gap:32px;font-size:14px;color:var(--ink)}
.hero-title{position:absolute;top:155px;width:1200px;text-align:center;font-size:52px;line-height:1.15}
.hero-copy{position:absolute;top:302px;left:300px;width:600px;text-align:center;font-size:13px}
.phone{position:absolute;left:250px;top:445px;width:293px;height:374px;border:3px solid #333;border-bottom:none;border-radius:38px 38px 0 0;background:#f8f4fb;overflow:hidden}
.phone .notch{position:absolute;left:110px;top:14px;width:74px;height:16px;border-radius:9px;background:#111}
.field{height:22px;border:1px solid #ccc;background:#fff;border-radius:2px}
.dash{position:absolute;left:545px;top:506px;width:408px;height:284px;background:#fff;box-shadow:0 2px 8px rgba(0,0,0,.12);font-size:6px;color:#555}
.ring{position:absolute;border-radius:50%;border:10px solid var(--blue)}

/* overview */
.sec-title{position:absolute;width:1200px;text-align:center;font-size:44px;line-height:1.15}
.illus{position:absolute;left:108px;top:1130px;width:440px;height:432px;border-radius:50%/40%;background:radial-gradient(ellipse at 50% 60%,#e9e9ef 0%,#f3f4f7 60%,#fff 100%)}
.benefit{position:absolute;width:221px;height:107px;background:var(--card);border-radius:5px;padding:22px 14px}
.benefit h3{font-size:16px;margin-bottom:10px}
.benefit p{font-size:10px;line-height:1.6}

/* features */
.band{position:absolute;left:0;top:1695px;width:1200px;height:653px;background:var(--blue)}
.band .ghost{position:absolute;left:270px;top:40px;width:600px;height:600px;border-radius:50%;border:70px solid rgba(255,255,255,.06)}
.feature{position:absolute;background:var(--card-soft);border-radius:10px;padding:50px 30px}
.feature .icon{width:68px;height:68px;border-radius:8px;background:#fff;display:flex;align-items:center;justify-content:center;margin-bottom:30px}
.feature h3{font-size:16px;margin-bottom:22px}
.feature p{font-size:11.5px;line-height:1.6}

/* how it works */
.step h3{font-size:19px;margin-bottom:16px}
.step p{font-size:13.5px;width:380px;line-height:1.55}
.step .more{display:block;margin-top:16px;font-size:13px;font-weight:700;color:var(--ink)}
.photo{position:absolute;width:384px;height:212px}
.num{position:absolute;left:570px;width:60px;text-align:center;font-size:28px;color:var(--blue)}
.timeline{position:absolute;left:599px;top:2675px;height:390px;border-left:2px dashed var(--blue)}

/* cta + footer */
.footer{position:absolute;left:0;top:3418px;width:1200px;height:564px;background:var(--dark)}
.cta{position:absolute;left:125px;top:3278px;width:950px;height:261px;background:var(--card)}
.quick a{display:block;color:#fff;font-size:14px;text-decoration:none;margin-bottom:14px}
.social{width:30px;height:30px;border-radius:50%;border:1.5px solid #fff}
.legal{position:absolute;top:3982px;left:0;width:1200px;height:61px;background:#fff;text-align:center;font-size:13px;padding-top:18px;color:var(--ink)}
</style>
</head>
<body>

<!-- HERO -->
<section class="hero">
  <div class="brand abs" style="left:125px;top:20px"><span class="dot"></span>qGuestly</div>
  <nav class="nav-links"><span>Home</span><span>Pricing</span><span>Feature</span><span>Blog</span></nav>
  <span class="btn btn-line" style="left:853px;top:23px;width:100px;height:37px">Login</span>
  <span class="btn btn-solid" style="left:975px;top:23px;width:100px;height:37px">Free Trial</span>

  <h1 class="hero-title"><span class="hl">Sign In Smarter Not</span><br>Harder.</h1>
  <p class="hero-copy">Lorem Ipsum is simply dummy text of the printing and typesetting industry. Lorem Ipsum has been the industry's standard dummy text ever since the 1500s</p>
  <span class="btn btn-solid" style="left:409px;top:381px;width:219px;height:37px">Start your 15 day free trial</span>
  <span class="btn btn-line" style="left:650px;top:381px;width:141px;height:37px">Buy Now</span>

  <div class="phone">
    <span class="abs" style="left:33px;top:14px;font-size:13px">2:10</span>
    <span class="notch"></span>
    <div class="abs" style="top:54px;width:100%;text-align:center;font-size:17px;color:#333">◯ qGuestly</div>
    <div class="abs" style="top:86px;width:100%;text-align:center;font-size:13px;font-weight:600;color:#222">Log into your Account</div>
    <div class="abs" style="top:106px;left:20px;right:20px;text-align:center;font-size:6.5px;color:#777">Log in to view visitors, manage your locations and connected devices.</div>
    <div class="abs" style="top:135px;left:0;width:100%;height:240px;background:#fff;padding:12px 32px;font-size:7px;color:#444">
      <div>Email Address</div><div class="field" style="margin:4px 0 14px"></div>
      <div>Password</div><div class="field" style="margin:4px 0 4px"></div>
      <div style="text-align:right;color:var(--purple)">Forgot Password?</div>
      <div style="margin-top:10px;height:22px;background:var(--purple);color:#fff;text-align:center;line-height:22px">Login</div>
      <div style="margin-top:18px;text-align:center;color:#888">Don't have an account? <span style="color:var(--purple)">Sign Up</span></div>
    </div>
  </div>

  <div class="dash">
    <div class="abs" style="left:8px;top:6px;font-size:10px;color:#333">◯ qGuestly</div>
    <div class="abs" style="right:6px;top:4px">Hi, Admin · Logout</div>
    <div class="abs" style="left:10px;top:26px;display:flex;gap:22px"><span>Today</span><span>Reports</span><span>Manage</span></div>
    <div class="abs" style="left:0;top:38px;width:100%;border-top:1px solid #eee"></div>
    <div class="abs" style="left:20px;top:44px">Manage › Locations › Head Office › Details</div>
    <div class="abs" style="left:20px;top:64px;line-height:2.6">
      <div style="color:var(--purple)">Details</div><div>Groups</div><div>Branding</div><div>Custom Fields</div><div>Messages</div><div>Privacy</div><div>Badges</div><div>Features</div><div>Devices</div><div>Sign In Route</div>
    </div>
    <div class="abs" style="left:112px;top:64px;width:280px">
      <div style="font-size:8px;color:#222">General</div>
      <div style="margin:4px 0 8px;color:#999">Set up the basic details of your location.</div>
      <div>Site name</div><div class="field" style="height:12px;margin:2px 0 6px"></div>
      <div>Site address</div><div class="field" style="height:44px;margin:2px 0 6px"></div>
      <div>Timezone</div><div class="field" style="height:12px;margin:2px 0 6px"></div>
      <div>Language</div><div class="field" style="height:12px;margin:2px 0 6px;border-color:#333"></div>
      <div style="display:flex;gap:8px"><div style="flex:1">Reply to name<div class="field" style="height:12px"></div></div><div style="flex:1">Reply to email<div class="field" style="height:12px"></div></div></div>
      <div style="margin:8px 0 0 auto;width:42px;height:10px;background:var(--purple)"></div>
    </div>
  </div>
  <div class="ring" style="left:900px;top:450px;width:108px;height:108px"></div>
</section>

<!-- OVERVIEW -->
<h2 class="sec-title" style="top:906px"><span class="hl">Enhance Security with Our Visitor</span><br>Tracking Systems.</h2>
<div class="illus" role="img" aria-label="Illustration of a visitor using a check-in kiosk screen beside a staff member"></div>
<h3 class="abs" style="left:611px;top:1090px;font-size:28px">What is qGuestly?</h3>
<p class="abs" style="left:611px;top:1143px;width:440px;font-size:13px">Lorem Ipsum is simply dummy text of the printing and typesetting industry. Lorem Ipsum has been the industry's standard dummy text ever since the 1500s, when an unknown printer took a galley of type and scrambled it to make a type specimen book.</p>
<div class="benefit" style="left:611px;top:1268px"><h3>Enhanced Security</h3><p>Lorem Ipsum is simply dummy text of the printing and typesetting industry.</p></div>
<div class="benefit" style="left:853px;top:1268px"><h3>Easy Integration</h3><p>Lorem Ipsum is simply dummy text of the printing and typesetting industry.</p></div>
<div class="benefit" style="left:611px;top:1396px"><h3>Operational Efficiency</h3><p>Lorem Ipsum is simply dummy text of the printing and typesetting industry.</p></div>
<span class="btn btn-solid" style="left:611px;top:1540px;width:124px;height:37px">Read More</span>

<!-- FEATURES -->
<section class="band">
  <div class="ghost"></div>
  <h2 class="sec-title" style="top:85px;color:#fff">Mobile Access for On the Go<br>Management</h2>
</section>
<div class="feature" style="left:125px;top:1937px;width:302px;height:306px">
  <div class="icon"><svg width="40" height="30" viewBox="0 0 40 30" fill="none" stroke="#333" stroke-width="2"><path d="M2 8h8l10 10 6-4 6 6M38 8h-8l-8 6"/><rect x="2" y="6" width="6" height="14"/><rect x="32" y="6" width="6" height="14"/></svg></div>
  <h3>Contactless Sign-In</h3>
  <p>Lorem Ipsum is simply dummy text of the printing and typesetting industry. Lorem Ipsum has been the industry's standard dummy text ever since the 1500s,</p>
</div>
<div class="feature" style="left:448px;top:1937px;width:304px;height:310px">
  <div class="icon"><svg width="32" height="32" viewBox="0 0 32 32" fill="none" stroke="#333" stroke-width="2"><path d="M8 22V14a8 8 0 0116 0v8l2 3H6z"/><path d="M13 27a3 3 0 006 0"/></svg></div>
  <h3>Real-Time Alerts</h3>
  <p>Lorem Ipsum is simply dummy text of the printing and typesetting industry. Lorem Ipsum has been the industry's standard dummy text ever since the 1500s,</p>
</div>
<div class="feature" style="left:772px;top:1937px;width:303px;height:315px">
  <div class="icon"><svg width="26" height="32" viewBox="0 0 26 32" fill="none" stroke="#333" stroke-width="2"><rect x="2" y="2" width="22" height="28"/><path d="M7 24v-5M12 24v-9M17 24v-7M7 8h12"/></svg></div>
  <h3>Comprehensive Reporting</h3>
  <p>Lorem Ipsum is simply dummy text of the printing and typesetting industry. Lorem Ipsum has been the industry's standard dummy text ever since the 1500s,</p>
</div>

<!-- HOW IT WORKS -->
<h2 class="sec-title" style="top:2438px"><span class="hl">How It</span> Works</h2>
<div class="step abs" style="left:125px;top:2585px"><h3>Professional Welcome</h3><p>Lorem Ipsum is simply dummy text of the printing and typesetting industry. Lorem Ipsum has been the industry's standard dummy text ever since the 1500s,</p><span class="more">Read More</span></div>
<div class="photo" style="left:691px;top:2543px;background:linear-gradient(120deg,#5b6f82 0%,#a7b3bd 45%,#2a2f38 100%)" role="img" aria-label="Photo of a businessman offering a handshake in an office"></div>
<div class="photo" style="left:125px;top:2755px;background:linear-gradient(110deg,#8a5a34 0%,#c89a6d 45%,#e7e2d6 100%)" role="img" aria-label="Photo of a woman scanning a code at a reception desk with her phone"></div>
<div class="step abs" style="left:691px;top:2796px"><h3>Smooth Entry, Effortless Check-In</h3><p>Lorem Ipsum is simply dummy text of the printing and typesetting industry. Lorem Ipsum has been the industry's standard dummy text ever since the 1500s,</p><span class="more">Read More</span></div>
<div class="photo" style="left:691px;top:2966px;background:radial-gradient(circle at 25% 40%,#f2c79a 0%,#8a5d45 35%,#3f3a40 100%)" role="img" aria-label="Photo of a team meeting around a table with a glowing digital network overlay"></div>
<div class="step abs" style="left:125px;top:3008px"><h3>Future-Ready Solutions</h3><p>Lorem Ipsum is simply dummy text of the printing and typesetting industry. Lorem Ipsum has been the industry's standard dummy text ever since the 1500s,</p><span class="more">Read More</span></div>
<div class="timeline"></div>
<span class="num" style="top:2628px;background:#fff">01</span>
<span class="num" style="top:2840px;background:#fff">02</span>
<span class="num" style="top:3052px;background:#fff">03</span>

<!-- CTA + FOOTER -->
<footer class="footer"></footer>
<section class="cta">
  <h2 class="abs" style="left:60px;top:40px;font-size:44px"><span class="hl">Start Your 15 Day</span> Free Trial</h2>
  <p class="abs" style="left:60px;top:118px;font-size:13px">Lorem Ipsum is simply dummy text of the printing and typesetting industry.</p>
  <span class="btn btn-solid" style="left:60px;top:174px;width:182px;height:36px">Schedule A Demo</span>
  <span class="btn btn-line" style="left:262px;top:174px;width:143px;height:36px">Buy Now</span>
  <div class="ring" style="left:680px;top:32px;width:206px;height:196px;border-width:14px"></div>
</section>

<div class="brand abs" style="left:125px;top:3652px;color:#fff"><span class="dot"></span>qGuestly</div>
<p class="abs" style="left:125px;top:3716px;width:280px;font-size:13px;color:#fff">Lorem Ipsum is simply dummy text of the printing and typesetting industry. Lorem Ipsum has been the industry's standard dummy text ever since the 1500s,</p>
<div class="abs" style="left:125px;top:3823px;display:flex;gap:12px"><span class="social"></span><span class="social"></span><span class="social"></span><span class="social"></span></div>
<h3 class="abs" style="left:497px;top:3660px;font-size:19px;color:#fff">Quick Links</h3>
<nav class="quick abs" style="left:497px;top:3707px"><a>Home</a><a>Pricing</a><a>Feature</a><a>Blog</a><a>Main Goal</a><a>Login</a></nav>

<div class="abs" style="left:780px;top:3660px;width:295px;height:322px;border:3px solid #111;border-bottom:none;border-radius:40px 40px 0 0;background:#fff;overflow:hidden">
  <span class="abs" style="left:36px;top:16px;font-size:13px">2:10</span>
  <span class="abs" style="left:108px;top:14px;width:78px;height:18px;border-radius:9px;background:#111"></span>
  <div class="abs" style="top:56px;width:100%;text-align:center;font-size:28px;color:#333">◯ qGuestly</div>
  <div class="abs" style="left:14px;top:118px;right:14px;height:200px;font-size:5px;color:#666">
    <div>◯ qGuestly</div>
    <div style="margin-top:14px;display:flex;gap:10px"><div style="line-height:2.4"><div style="color:var(--purple)">Details</div><div>Groups</div><div>Branding</div><div>Fields</div><div>Messages</div><div>Privacy</div><div>Badges</div><div>Devices</div></div>
    <div style="flex:1;margin-left:30px">General<div class="field" style="height:8px;margin:6px 0"></div><div class="field" style="height:24px;margin:6px 0"></div><div class="field" style="height:8px;margin:6px 0"></div><div class="field" style="height:8px;margin:6px 0;border-color:#333"></div><div style="margin:8px 0 0 auto;width:24px;height:6px;background:var(--purple)"></div></div></div>
  </div>
</div>

<div class="legal">© 2024 Northvale Apps Ltd is part of the qGuestly suite of brands providing global, cloud-based solutions to manage visitors</div>

</body>
</html>
```